依頼詳細
現サイト http://www.kozanso-hp.jp/

今回のリニューアルでは基調色を「緑以外」というご希望です。
素材は下記からダウンロードしていただけます。
※容量が大きいです。施設パンフなどに使ったものを一切合切入れてあります。

自由な発想でデザインしてみてください。
シンプル系もありだと思います。
サイトURL
http://www.kozanso-hp.jp/
ページ数
1ページ
希望イメージ
シンプル 複雑
単色 カラフル
暗い 明るい
日常 高級
遊び心 厳粛
未来的 伝統的
女性的 男性的
希望する色
赤系、水色系、黄・オレンジ系
納品ファイル
• フォトショップ形式 (.psd)
• PNG形式 (.png)
補足説明
サイトマップを添付致します。
★タイトなスケジュールで申し訳ありませんが、ぜひご提案くださいませ。
よろしくお願い致します!
素材のダウンロード先を記入し忘れておりました。申し訳ありません。
https://dl3.fomvault.jp/get/9b2d17ac53e04f6ab81c92d7e4f0a6b3.html
(パスワード: peWoxiMt)
サイトマップの添付を追加致しました。
選定確約という機能があることを知りました。チェックをいれましたので必ず当選者様を選定致します。
■ 選んだ理由

tokinekaho様
お世話になります。今回のご提案をクライアント様に気に入っていただきました。修正なしでこのままでOKでございます。
シンプル系がやはりクライアント様が選んだ一番の理由だったと思います。
すばらしいです。

■ 提案者全員のお礼・コメント

弊社判断で当選を決定できなかったのですが、先方クライアント様との打ち合わせで、「おそらくこれが一番気に入られるかな」という印象でした。
昨日、プリントアウトしてプリンターの加減も含めた中で、当選決定となりました。やはりディレクションの重要さとそれをクラウドソーシングに伝える難しさや良さも同時に感じました。
今回は本当にありがとうございます。
株式会社ケミノ 杉浦

```html
<!DOCTYPE html>
<html lang="ja">
<head>
<meta charset="utf-8">
<title>光山荘 | 介護サービス</title>
<link href="https://fonts.googleapis.com/css2?family=Noto+Sans+JP:wght@400;500;700&family=Noto+Serif+JP:wght@500;700&display=swap" rel="stylesheet">
<style>
:root{
  --orange:#ee8a3a;
  --orange-dark:#d8712a;
  --brown:#5b4631;
  --text:#4a3d30;
  --muted:#8a7b6a;
  --beige:#f3ecdf;
  --line:#e3d9c9;
  --white:#ffffff;
  --footer-bar:#6b5641;
}
*{box-sizing:border-box;margin:0;padding:0}
html,body{width:1200px;height:2180px;overflow:hidden}
body{font-family:"Noto Sans JP",sans-serif;color:var(--text);background:var(--white);font-size:14px;line-height:1.7}

.site-header{height:112px;display:flex;align-items:center;justify-content:space-between;padding:0 40px}
.corp{font-size:12px;color:var(--muted);line-height:1.6}
.brand{text-align:center;display:flex;align-items:center;gap:14px}
.brand .sub{font-size:11px;color:var(--muted)}
.brand .name{font-family:"Noto Serif JP",serif;font-size:34px;font-weight:700;color:var(--brown);letter-spacing:6px}
.brand .ruby{font-size:10px;color:var(--muted);display:block;letter-spacing:4px}
.contact{display:flex;align-items:center;gap:14px}
.tel small{display:block;font-size:11px;color:var(--muted);line-height:1.2}
.tel strong{font-family:"Noto Serif JP",serif;font-size:26px;color:var(--brown);letter-spacing:1px;line-height:1.2}
.btn{display:inline-flex;align-items:center;gap:6px;background:var(--orange);color:var(--white);font-size:13px;padding:8px 18px;border-radius:3px;text-decoration:none}

.global-nav{height:64px;border-top:1px solid var(--line);border-bottom:1px solid var(--line);display:flex;justify-content:center}
.global-nav a{flex:0 0 auto;width:148px;text-align:center;text-decoration:none;color:var(--brown);font-size:14px;line-height:1.3;padding-top:13px;border-right:1px solid var(--line);white-space:nowrap}
.global-nav a:first-child{border-left:1px solid var(--line);width:80px}
.global-nav a.wide{width:196px}
.global-nav a small{display:block;font-size:10px;color:var(--muted);margin-top:2px}

.hero{position:relative;height:650px}
.hero-photo{position:absolute;inset:0;background:linear-gradient(180deg,#8fc3e8 0%,#cfe4f1 35%,#7ea46a 60%,#56743f 78%,#bdb5a2 100%)}
.hero-badge{position:absolute;left:40px;top:30px;width:170px;height:170px;border-radius:50%;background:var(--orange);color:var(--white);text-align:center;padding-top:34px;font-size:13px;line-height:1.6}
.hero-badge em{display:block;font-style:normal;font-size:11px;letter-spacing:1px}
.hero-badge b{display:block;font-family:"Noto Serif JP",serif;font-size:18px;margin:4px 0}
.hero-copy{position:absolute;left:330px;top:120px;color:var(--white);text-align:center;width:520px}
.hero-copy p{font-family:"Noto Serif JP",serif;font-size:22px;letter-spacing:2px}
.hero-copy h1{font-family:"Noto Serif JP",serif;font-size:34px;font-weight:500;letter-spacing:3px}
.hero-thumbs{position:absolute;right:28px;top:20px;display:flex;flex-direction:column;gap:14px}
.hero-thumbs div{width:170px;height:105px;border:4px solid var(--white)}

.intro{position:relative;display:flex;gap:24px;padding:0 40px;margin-top:-14px}
.card{background:var(--white);border:1px solid var(--line);box-shadow:0 2px 6px rgba(0,0,0,.08)}
.care{width:620px;height:160px;display:flex;padding:18px 20px;gap:18px}
.care-text h2{font-family:"Noto Serif JP",serif;font-size:17px;color:var(--brown);border-bottom:1px solid var(--line);padding-bottom:4px;margin-bottom:8px}
.care-text p{font-size:12px;line-height:1.75;color:var(--text)}
.care-photo{width:180px;flex:0 0 180px;background:linear-gradient(160deg,#f4efe8,#d9cfc3)}
.news{flex:1;height:245px;padding:16px 20px;margin-top:-90px}
.news h2{font-family:"Noto Serif JP",serif;font-size:16px;color:var(--white);background:var(--orange);padding:4px 12px;margin-bottom:10px}
.news li{list-style:none;font-size:12px;border-bottom:1px dotted var(--line);padding:4px 0;line-height:1.5}
.news time{color:var(--orange-dark);font-size:11px;display:block}

.services{background:var(--beige);margin-top:30px;height:810px;padding-top:60px}
.section-title{text-align:center;font-family:"Noto Serif JP",serif;font-size:26px;color:var(--brown);letter-spacing:4px}
.section-title span{display:block;width:60px;height:2px;background:var(--orange);margin:12px auto 0}
.service-grid{display:grid;grid-template-columns:repeat(3,300px);gap:30px 38px;justify-content:center;margin-top:44px}
.service{background:var(--white);border:1px solid var(--line)}
.service .ph{height:236px}
.service h3{font-family:"Noto Serif JP",serif;font-size:16px;font-weight:500;color:var(--brown);text-align:center;padding:10px 0;white-space:nowrap}

.site-footer{height:360px;padding:40px 40px 0;position:relative}
.footer-top{display:flex;align-items:center;gap:60px;border-bottom:1px solid var(--line);padding-bottom:24px}
.footer-brand .corp{font-size:11px}
.footer-brand .name{font-family:"Noto Serif JP",serif;font-size:30px;font-weight:700;color:var(--brown);letter-spacing:5px}
.footer-brand address{font-style:normal;font-size:11px;color:var(--muted)}
.footer-links{display:grid;grid-template-columns:repeat(4,auto);gap:8px 40px;padding:24px 0 0 40px;font-size:13px}
.footer-links a{color:var(--text);text-decoration:none}
.footer-links a::before{content:"›";color:var(--orange);margin-right:6px}
.copyright{position:absolute;left:0;right:0;bottom:0;height:44px;background:var(--footer-bar);color:var(--white);font-size:11px;text-align:center;line-height:44px}
</style>
</head>
<body>

<header class="site-header">
  <div class="corp">社会福祉法人 光和会<br>特別養護老人ホーム</div>
  <div class="brand">
    <span class="sub">特別養護老人ホーム</span>
    <div><span class="ruby">こうざんそう</span><span class="name">光山荘</span></div>
  </div>
  <div class="contact">
    <div class="tel"><small>入居のご相談・ご見学は</small><strong>TEL 0745-00-3150</strong></div>
    <a class="btn" href="#">
      <svg width="14" height="10" viewBox="0 0 14 10"><rect x=".5" y=".5" width="13" height="9" fill="none" stroke="#fff"/><path d="M.5 .5 7 6 13.5 .5" fill="none" stroke="#fff"/></svg>
      お問い合わせ</a>
  </div>
</header>

<nav class="global-nav">
  <a href="#">ホーム<small>Home</small></a>
  <a href="#">光山荘について<small>About us</small></a>
  <a href="#">ショートステイ<small>Short stay</small></a>
  <a href="#">デイサービス<small>Day service</small></a>
  <a class="wide" href="#">居宅介護支援・訪問ヘルプ<small>Home help</small></a>
  <a href="#">施設紹介・行事<small>Facilities</small></a>
  <a href="#">よくあるご質問<small>Q&amp;A</small></a>
</nav>

<section class="hero">
  <div class="hero-photo" role="img" aria-label="山々に囲まれた施設の外観と青空の写真"></div>
  <div class="hero-badge"><em>Comfortable life</em><b>快適な日々を</b>自然の中で穏やかに<br>過ごせる毎日を<br>お届けします</div>
  <div class="hero-copy"><p>信頼できる介護サービスの</p><h1>トータルコーディネーター</h1></div>
  <div class="hero-thumbs">
    <div role="img" aria-label="明るい廊下の写真" style="background:linear-gradient(160deg,#e9d9bf,#b58c5d)"></div>
    <div role="img" aria-label="居室内部の写真" style="background:linear-gradient(160deg,#f1e4cf,#c09a6b)"></div>
    <div role="img" aria-label="食堂の写真" style="background:linear-gradient(160deg,#e6d3b3,#a77a4a)"></div>
  </div>
</section>

<div class="intro">
  <div class="card care">
    <div class="care-text">
      <h2>ハートフルケア</h2>
      <p>光山荘は緑豊かな山あいに位置し、四季の移ろいを感じながら安心して暮らせる施設です。ご利用者様お一人おひとりの想いに寄り添い、心のこもった介護サービスをご提供いたします。</p>
    </div>
    <div class="care-photo" role="img" aria-label="介護職員が利用者に寄り添う写真"></div>
  </div>
  <div class="card news">
    <h2>新着情報</h2>
    <ul>
      <li><time>2016.08.18</time>新しいパンフレットができました。</li>
      <li><time>2016.08.10</time>夏祭りを開催しました。</li>
      <li><time>2016.07.25</time>ショートステイのご案内を更新しました。</li>
      <li><time>2016.06.15</time>新しいホームページを公開しました。</li>
    </ul>
  </div>
</div>

<section class="services">
  <h2 class="section-title">光山荘の介護サービス案内<span></span></h2>
  <div class="service-grid">
    <div class="service"><div class="ph" role="img" aria-label="特別養護老人ホームの室内写真" style="background:linear-gradient(160deg,#efe2c9,#b99364)"></div><h3>特別養護老人ホーム</h3></div>
    <div class="service"><div class="ph" role="img" aria-label="ショートステイ棟の外観写真" style="background:linear-gradient(180deg,#a9cbe6,#8a9d7a)"></div><h3>ショートステイ</h3></div>
    <div class="service"><div class="ph" role="img" aria-label="デイサービスの活動写真" style="background:linear-gradient(160deg,#f0dcc0,#c48f5c)"></div><h3>デイサービス</h3></div>
    <div class="service"><div class="ph" role="img" aria-label="居宅介護支援センターの外観写真" style="background:linear-gradient(180deg,#9cc4e4,#7f9b6e)"></div><h3>居宅介護支援センター・訪問ヘルプ</h3></div>
    <div class="service"><div class="ph" role="img" aria-label="施設周辺の山並みの写真" style="background:linear-gradient(180deg,#b9cbd6,#5d7452)"></div><h3>光山荘の四季</h3></div>
    <div class="service"><div class="ph" role="img" aria-label="アクセス周辺の風景写真" style="background:linear-gradient(180deg,#8fbde2,#6f9157)"></div><h3>アクセスマップ</h3></div>
  </div>
</section>

<footer class="site-footer">
  <div class="footer-top">
    <div class="footer-brand">
      <div class="corp">社会福祉法人 光和会<br>特別養護老人ホーム</div>
      <div class="name">光山荘</div>
      <address>〒639-0000 奈良県光山郡光山町1234番地</address>
    </div>
    <div class="tel"><small>入居のご相談・ご見学は</small><strong>TEL 0745-00-3150</strong></div>
    <a class="btn" href="#">お問い合わせ</a>
  </div>
  <div class="footer-links">
    <a href="#">光山荘について</a><a href="#">デイサービス</a><a href="#">居宅介護支援・訪問ヘルプ</a><a href="#">よくあるご質問</a>
    <a href="#">特別養護老人ホーム</a><a href="#">ショートステイ</a><a href="#">施設紹介・行事</a><a href="#">お問い合わせ</a>
  </div>
  <div class="copyright">Copyright © kozanso. All Rights Reserved.</div>
</footer>

</body>
</html>
```